Create a Flyer for a Darts Tournament

We need a Flyer for a Darts Tournament that is going to be organized by our darts department (logo attached). The name of the tournament is "3. KLW Dartsturnier". The Flyer should look modern, professional and in a way that everyone can see at the first impression that is has to do with dart sports. The logo of our department should be on the flyer as well. On the flyer we need an area where we can place some informations regarding the tournament (bullet points) etc. And a area where we can place informations regarding the registration progress (e.g. "Registration via E-Mail". Should fit well to our logo.

Target Market(s)

Darts Players for the Tournament

Font styles to use
Serif

Colors

Designer to choose colors to be used in the design.

Requirements
Must have
• Name of the Tournament, our Logo, place for some tournament details, link to our registration page (besucher.tv-halmerau.de). Should

```html
<!DOCTYPE html>
<html lang="de">
<head>
<meta charset="utf-8">
<title>3. KLW Dartsturnier – Flyer</title>
<link rel="stylesheet" href="https://fonts.googleapis.com/css2?family=Alfa+Slab+One&family=Bebas+Neue&family=Oswald:wght@200;500&family=Poppins:wght@400;600;700&display=swap">
<style>
  :root {
    --page-bg: #d6d6d6;
    --ink-dark: #08172a;
    --navy: #0b3f66;
    --sky: #00a8e8;
    --red: #e4102a;
    --white: #ffffff;
    --grey-text: #6b6b6b;
  }
  * { margin: 0; padding: 0; box-sizing: border-box; }
  html, body { width: 1200px; height: 950px; overflow: hidden; background: var(--page-bg); }
  .flyer {
    position: absolute; left: 250px; top: 22px;
    width: 700px; height: 906px;
    background: var(--white); overflow: hidden;
    font-family: "Poppins", sans-serif;
  }
  .side-column { position: absolute; left: 0; top: 0; width: 184px; height: 100%; background: var(--ink-dark); }
  .abs { position: absolute; }

  .title-number, .title-name {
    position: absolute; top: 58px;
    font-family: "Alfa Slab One", serif; font-size: 128px; line-height: 1;
    white-space: nowrap;
  }
  .title-number { left: 56px; color: var(--white); }
  .title-number .dot { color: var(--navy); }
  .title-name { left: 197px; color: var(--navy); letter-spacing: 0; }

  .club-mark { left: 532px; top: 70px; width: 140px; display: flex; flex-direction: column; align-items: center; gap: 8px; }
  .club-mark .disc { width: 70px; height: 70px; border-radius: 50%; background: var(--sky); }
  .club-mark .club-name { font-family: "Bebas Neue", sans-serif; font-size: 46px; color: var(--navy); line-height: 1; }

  .title-band { left: 0; top: 204px; width: 487px; height: 73px; background: var(--sky); box-shadow: 0 8px 10px -6px rgba(0,0,0,.35); }
  .title-band span { position: absolute; left: 58px; top: 4px; font-family: "Bebas Neue", sans-serif; font-size: 72px; line-height: 1; color: var(--white); letter-spacing: 1px; }

  .date-day { left: 56px; top: 300px; font-family: "Alfa Slab One", serif; font-size: 92px; line-height: 1; color: var(--white); }
  .date-weekday { left: 60px; top: 392px; font-family: "Bebas Neue", sans-serif; font-size: 32px; line-height: 1; color: var(--sky); }
  .date-month { left: 196px; top: 306px; font-family: "Alfa Slab One", serif; font-size: 48px; line-height: 1; color: var(--navy); }
  .date-year { left: 196px; top: 354px; font-family: "Oswald", sans-serif; font-weight: 200; font-size: 60px; line-height: 1; color: var(--ink-dark); }

  .time-block { top: 310px; }
  .time-block .label { font-family: "Bebas Neue", sans-serif; font-size: 37px; line-height: 1; color: var(--ink-dark); }
  .time-tag {
    margin-top: 4px; display: inline-block; height: 23px; padding: 0 16px 0 7px;
    background: var(--red); color: var(--white);
    font-family: "Bebas Neue", sans-serif; font-size: 21px; line-height: 25px;
    clip-path: polygon(0 0, 100% 0, 88% 50%, 100% 100%, 0 100%);
  }
  .time-tag small { font-size: 12px; }
  .time-admission { left: 350px; }
  .time-start { left: 472px; }

  .format-list { left: 60px; top: 454px; color: var(--white); font-size: 10.5px; font-weight: 500; }
  .format-list .phase { margin-bottom: 3px; }
  .format-tags { display: flex; gap: 7px; margin-bottom: 10px; }
  .format-tags span {
    width: 30px; height: 14px; background: var(--sky); color: var(--ink-dark);
    font-family: "Bebas Neue", sans-serif; font-size: 14px; line-height: 15px; padding-left: 4px;
    clip-path: polygon(0 0, 100% 0, 86% 50%, 100% 100%, 0 100%);
  }

  .highlights { left: 60px; top: 557px; width: 112px; list-style: none; }
  .highlights li { position: relative; padding-left: 12px; padding-bottom: 8px; margin-bottom: 8px; border-bottom: 1px solid rgba(255,255,255,.18); }
  .highlights li:last-child { border-bottom: none; }
  .highlights .tick { position: absolute; left: 0; top: 2px; width: 7px; height: 7px; }
  .highlights strong { display: block; color: var(--sky); font-size: 8.5px; font-weight: 700; line-height: 1.25; }
  .highlights p { color: var(--white); font-size: 8.5px; line-height: 1.25; }

  .event-type { left: 197px; top: 448px; }
  .event-type .kind { font-family: "Bebas Neue", sans-serif; font-size: 42px; line-height: 1; color: var(--sky); }
  .event-type .sub { font-weight: 700; font-size: 15px; letter-spacing: 4px; color: var(--ink-dark); line-height: 1.1; }
  .event-type .note { font-size: 11.5px; color: var(--grey-text); margin-top: 2px; }

  .venue { left: 198px; top: 550px; display: flex; gap: 9px; }
  .venue p { font-weight: 600; font-size: 16px; line-height: 17px; color: var(--navy); }

  .board-scene { left: 0; top: 0; }
  .dart-visual { left: 203px; top: 616px; width: 190px; height: 117px; border-radius: 60px 20px 20px 60px; background: linear-gradient(90deg, #3d85d8, #1d5fb8 70%, #a8a8a8); }

  .info-block { left: 198px; top: 768px; }
  .info-block .label { font-size: 9px; font-weight: 600; letter-spacing: 1.5px; color: var(--ink-dark); }
  .info-block a { font-size: 12.5px; font-weight: 600; color: var(--sky); text-decoration: none; }

  .register-band {
    left: 60px; top: 811px; width: 416px; height: 30px; background: var(--red);
    clip-path: polygon(0 0, 100% 0, 97% 100%, 0 100%, 3% 50%);
    display: flex; align-items: center; padding-left: 26px; gap: 12px;
    font-family: "Bebas Neue", sans-serif; font-size: 23px; color: var(--white); line-height: 1;
  }
  .register-band .divider { width: 1px; height: 20px; background: var(--white); }

  .register-mail { left: 60px; top: 853px; font-size: 9.5px; font-weight: 600; color: var(--white); }
  .register-arrow { left: 184px; top: 856px; width: 0; height: 0; border-top: 7px solid transparent; border-bottom: 7px solid transparent; border-left: 6px solid var(--sky); }
  .register-link { left: 197px; top: 848px; font-size: 15px; font-weight: 600; color: var(--ink-dark); }
</style>
</head>
<body>
<main class="flyer">
  <div class="side-column"></div>

  <h1>
    <span class="title-number">3<span class="dot">.</span></span>
    <span class="title-name">KLW</span>
  </h1>

  <div class="abs club-mark">
    <span class="disc"></span>
    <span class="club-name">KLW</span>
  </div>

  <svg class="abs board-scene" width="700" height="906" viewBox="0 0 700 906">
    <defs>
      <path id="capacity-arc" d="M418 544 A290 290 0 0 1 809 447"/>
      <radialGradient id="board-tones" cx="50%" cy="50%" r="50%">
        <stop offset="0" stop-color="#1f6fc9"/>
        <stop offset=".55" stop-color="#c9d3de"/>
        <stop offset=".85" stop-color="#2a73c4"/>
        <stop offset="1" stop-color="#1b1b1b"/>
      </radialGradient>
    </defs>
    <circle cx="664" cy="698" r="313" fill="var(--sky)"/>
    <circle cx="664" cy="698" r="277" fill="none" stroke="var(--white)" stroke-width="3"/>
    <circle cx="664" cy="698" r="240" fill="url(#board-tones)" role="img" aria-label="Foto einer Steeldart-Scheibe in Blau, Weiß und Rot"/>
    <circle cx="388" cy="698" r="15" fill="var(--white)"/>
    <text font-family="Poppins, sans-serif" font-weight="700" font-size="13" letter-spacing="3.5">
      <textPath href="#capacity-arc"><tspan fill="#ffffff">MAXIMAL </tspan><tspan fill="#08172a">48 TEILNEHMER</tspan></textPath>
    </text>
  </svg>

  <div class="abs title-band"><span>DARTSTURNIER</span></div>

  <div class="abs date-day">25</div>
  <div class="abs date-weekday">SAMSTAG</div>
  <div class="abs date-month">JAN</div>
  <div class="abs date-year">2025</div>

  <div class="abs time-block time-admission">
    <div class="label">EINLASS</div>
    <div class="time-tag">16:00 <small>UHR</small></div>
  </div>
  <div class="abs time-block time-start">
    <div class="label">TURNIERBEGINN</div>
    <div class="time-tag">17:00 <small>UHR</small></div>
  </div>

  <div class="abs format-list">
    <div class="phase">Gruppenphase</div>
    <div class="format-tags"><span>301</span><span>DO</span><span>BO3</span></div>
    <div class="phase">KO-Phase</div>
    <div class="format-tags"><span>501</span><span>DO</span><span>BO5</span></div>
  </div>

  <ul class="abs highlights">
    <li><svg class="tick" viewBox="0 0 10 10"><circle cx="5" cy="5" r="5" fill="#e4102a"/><path d="M2.6 5.2 4.3 6.8 7.4 3.4" stroke="#fff" stroke-width="1.5" fill="none"/></svg>
      <strong>Opening Ceremony</strong><p>Kick-off with player introductions and tournament rules.</p></li>
    <li><svg class="tick" viewBox="0 0 10 10"><circle cx="5" cy="5" r="5" fill="#e4102a"/><path d="M2.6 5.2 4.3 6.8 7.4 3.4" stroke="#fff" stroke-width="1.5" fill="none"/></svg>
      <strong>Highest Score Challenge</strong><p>Prize awarded for the highest single score.</p></li>
    <li><svg class="tick" viewBox="0 0 10 10"><circle cx="5" cy="5" r="5" fill="#e4102a"/><path d="M2.6 5.2 4.3 6.8 7.4 3.4" stroke="#fff" stroke-width="1.5" fill="none"/></svg>
      <strong>Doubles Knockout Rounds</strong><p>Teams compete in exciting elimination rounds.</p></li>
    <li><svg class="tick" viewBox="0 0 10 10"><circle cx="5" cy="5" r="5" fill="#e4102a"/><path d="M2.6 5.2 4.3 6.8 7.4 3.4" stroke="#fff" stroke-width="1.5" fill="none"/></svg>
      <strong>Championship Match</strong><p>The grand finale to crown the tournament winner.</p></li>
  </ul>

  <div class="abs event-type">
    <div class="kind">STEEL DARTS</div>
    <div class="sub">HOBBYTURNIER</div>
    <div class="note">(keine Ligaspieler)</div>
  </div>

  <div class="abs venue">
    <svg width="32" height="46" viewBox="0 0 32 46"><path d="M16 0C7 0 0 7 0 16c0 11 16 30 16 30s16-19 16-30C32 7 25 0 16 0z" fill="#e4102a"/><circle cx="16" cy="15" r="6" fill="#fff"/></svg>
    <p>MZH in 71234<br>Halmerau<br>Süd</p>
  </div>

  <div class="abs dart-visual" role="img" aria-label="Foto eines blauen Dartpfeils im Flug"></div>

  <div class="abs info-block">
    <div class="label">INFOS</div>
    <a href="#">darts.tv-halmerau.de</a>
  </div>

  <div class="abs register-band">
    <span>ANMELDUNG</span><span class="divider"></span><span>BESUCHER.TV-HALMERAU.DE</span>
  </div>

  <div class="abs register-mail">Anmeldung per E-Mail</div>
  <div class="abs register-arrow"></div>
  <div class="abs register-link">besucher.tv-halmerau.de</div>
</main>
</body>
</html>
```